female esthetician looking for an impact business card

I an an expert in skin care industry with high experience in NYC.I want my business card to look professional , an impact at first look. I do want a combination between white and gold . I believe the font will be great if is gold.. The Fonts are also important. MARISELA VONDRAKE (SKIN CARE BOUTIQUE)

THIS SHOULD BE THE BUSINESS NAME, and should be placed on th eback of the card.
IN front m, the name MARISELA VONDRAKE - ESTHETCIAN

BY APPOINTMENTS ONLY: 555.218.9031

Target Market(s)

HIGH END CLIENTELE

Contact Information for Business Card

iT WILL BE on a luxury paper. I neeed the wow feeling

Requirements
Should not have
• pictures

```html
<!DOCTYPE html>
<html lang="en">
<head>
<meta charset="utf-8">
<title>Marisela Vondrake – Business Card</title>
<link rel="stylesheet" href="https://fonts.googleapis.com/css2?family=Permanent+Marker&family=Dancing+Script:wght@400&display=swap">
<style>
  :root {
    --backdrop: #2a2c30;
    --card-white: #ffffff;
    --gold-dark: #c07a12;
    --gold-mid: #e5a21f;
    --gold-light: #f6cf4a;
    --ink: #1c1c1c;
    --mint: #cdeee2;
    --mint-soft: #e6f7f0;
  }
  html, body {
    margin: 0;
    padding: 0;
    width: 1200px;
    height: 900px;
    overflow: hidden;
    background: var(--backdrop);
  }
  .canvas {
    position: relative;
    width: 1200px;
    height: 900px;
  }
  .business-card {
    position: absolute;
    left: 150px;
    top: 190px;
    width: 900px;
    height: 520px;
    box-sizing: border-box;
    padding: 16px;
    background: linear-gradient(135deg, var(--gold-dark) 0%, var(--gold-light) 30%, var(--gold-mid) 55%, var(--gold-light) 78%, var(--gold-dark) 100%);
    box-shadow: 0 18px 40px rgba(0,0,0,0.45);
  }
  .card-face {
    position: relative;
    width: 100%;
    height: 100%;
    background: var(--card-white);
    overflow: hidden;
  }
  .brand-mark-area {
    position: absolute;
    left: 50px;
    top: 30px;
    width: 240px;
    height: 290px;
    border-radius: 40px;
    background: radial-gradient(circle at 45% 70%, var(--mint) 0%, var(--mint-soft) 60%, var(--card-white) 100%);
  }
  .identity {
    position: absolute;
    left: 320px;
    right: 60px;
    top: 160px;
  }
  .holder-name {
    margin: 0;
    font-family: "Permanent Marker", cursive;
    font-weight: 400;
    font-size: 36px;
    line-height: 1.2;
    letter-spacing: 3px;
    color: var(--ink);
    white-space: nowrap;
  }
  .holder-role {
    margin: 10px 0 0 30px;
    font-family: "Dancing Script", cursive;
    font-size: 30px;
    line-height: 1.2;
    letter-spacing: 1px;
    color: var(--ink);
    white-space: nowrap;
  }
  .appointment-line {
    margin: 22px 0 0 30px;
    font-family: "Dancing Script", cursive;
    font-size: 24px;
    line-height: 1.2;
    color: var(--gold-dark);
    white-space: nowrap;
  }
</style>
</head>
<body>
  <main class="canvas">
    <section class="business-card">
      <div class="card-face">
        <div class="brand-mark-area" role="img" aria-label="Mint line-drawn flower emblem"></div>
        <div class="identity">
          <h1 class="holder-name">MARISELA VONDRAKE</h1>
          <p class="holder-role">esthetician · skin care expert</p>
          <p class="appointment-line">by appointment only: 555.218.9031</p>
        </div>
      </div>
    </section>
  </main>
</body>
</html>
```